Bramble Nook Complementary Pass

I’d like a complimentary pass for any 30-minute Bramble Nook session. Choose one of the following options: Infrared Sauna with Red Light, Massage Chair Velquist Compression Therapy, or Paraffin Wax Hand Bath.

Please incorporate the logo and brand colors into your design. I’d like a square image that will be printed on square business cards (no rectangles).

Please refer to the logo and menu for more details.

See discretion

```html
<!DOCTYPE html>
<html lang="en">
<head>
<meta charset="utf-8">
<title>Meridel Physical Therapy – Bramble Nook Pass</title>
<link href="https://fonts.googleapis.com/css2?family=Nunito:ital,wght@0,400;0,600;0,700;1,700&family=Oswald:wght@500&family=Allura&family=Open+Sans:ital,wght@0,400;1,400;1,700&display=swap" rel="stylesheet">
<style>
  :root {
    --purple: #432f85;
    --purple-soft: #5a4a9c;
    --orange: #ef5a3a;
    --ink: #1d1d2b;
    --card: #fdfcfd;
    --backdrop: #c3c5c7;
  }
  * { box-sizing: border-box; margin: 0; padding: 0; }
  html, body { width: 1200px; height: 900px; overflow: hidden; }
  body { background: var(--backdrop); position: relative; font-family: "Nunito", sans-serif; }

  .card {
    position: absolute;
    width: 460px; height: 458px;
    background: var(--card);
    border-radius: 46px;
    overflow: hidden;
  }

  /* Front */
  .card--front { left: 113px; top: 222px; }
  .front-dot {
    position: absolute; left: 198px; top: 92px;
    width: 64px; height: 64px; border-radius: 50%;
    background: var(--orange);
  }
  .front-name {
    position: absolute; left: 0; right: 0; top: 180px;
    text-align: center; color: var(--purple);
    font-family: "Nunito", sans-serif; font-weight: 700; font-size: 92px; line-height: 1;
    letter-spacing: -1px;
  }
  .front-tagline {
    position: absolute; left: 0; right: 0; top: 333px;
    text-align: center; color: var(--purple-soft);
    font-family: "Oswald", sans-serif; font-weight: 500; font-size: 28px; letter-spacing: 3px;
  }

  /* Back */
  .card--back { left: 627px; top: 220px; width: 461px; height: 461px; }
  .brand {
    position: absolute; left: 0; right: 0; top: 20px;
    display: flex; justify-content: center; align-items: center; gap: 8px;
  }
  .brand__dot { width: 16px; height: 16px; border-radius: 50%; background: var(--orange); }
  .brand__name { color: var(--purple); font-weight: 700; font-size: 30px; line-height: 1; }

  .lounge-title {
    position: absolute; left: 0; right: 0; top: 62px;
    text-align: center; color: var(--purple);
    font-family: "Allura", cursive; font-size: 62px; line-height: 1;
  }
  .pass-rule {
    position: absolute; left: 0; right: 0; top: 143px;
    display: flex; align-items: center; gap: 6px;
  }
  .pass-rule::before, .pass-rule::after { content: ""; flex: 1; height: 1px; background: var(--purple); }
  .pass-rule span { color: var(--orange); font-weight: 700; font-size: 13.5px; }

  .options {
    position: absolute; left: 28px; top: 169px; list-style: none;
    font-family: "Open Sans", sans-serif; font-size: 12.5px; color: var(--ink);
  }
  .options li { height: 18.5px; display: flex; align-items: center; gap: 7px; }
  .options li::before { content: ""; width: 5px; height: 5px; border-radius: 50%; background: var(--purple); }

  .prices { position: absolute; left: 234px; right: 26px; top: 182px; font-family: "Open Sans", sans-serif; }
  .prices .row { display: flex; justify-content: space-between; height: 18px; align-items: center; font-size: 12px; }
  .prices .label { font-style: italic; font-weight: 700; color: var(--ink); }
  .prices .label--note { font-weight: 400; padding-left: 27px; }
  .prices .price { font-weight: 700; color: var(--purple); font-family: "Nunito", sans-serif; }
  .prices .row--gap { margin-top: 8px; }

  .person { position: absolute; left: 0; right: 0; top: 260px; text-align: center; }
  .person__name { color: var(--orange); font-weight: 700; font-size: 24px; letter-spacing: 1px; line-height: 1.2; }
  .person__role { color: var(--purple); font-size: 15px; letter-spacing: .6px; line-height: 18px; margin-top: 5px; }
  .person__rule { width: 102px; height: 2px; background: var(--orange); margin: 5px auto 0; }

  .contact { position: absolute; left: 28px; top: 350px; color: var(--purple); font-size: 14px; }
  .contact li { list-style: none; display: flex; align-items: center; gap: 8px; height: 22px; }
  .contact svg { width: 13px; height: 13px; fill: var(--orange); flex: none; }
  .contact .phone { letter-spacing: 2.5px; font-weight: 600; }

  .address { position: absolute; right: 28px; top: 348px; text-align: right; color: var(--purple); font-size: 14.5px; line-height: 21px; }
  .address__label { color: var(--orange); font-weight: 700; font-size: 17px; }

  .footer-band { position: absolute; left: 0; right: 0; bottom: 0; height: 34px; background: var(--purple); }
  .footer-band svg { position: absolute; left: 199px; top: 0; }
</style>
</head>
<body>

  <section class="card card--front" aria-label="Card front">
    <div class="front-dot"></div>
    <div class="front-name">meridel</div>
    <div class="front-tagline">PHYSICAL THERAPY</div>
  </section>

  <section class="card card--back" aria-label="Card back">
    <div class="brand"><span class="brand__dot"></span><span class="brand__name">meridel</span></div>
    <h1 class="lounge-title">Bramble Nook</h1>
    <div class="pass-rule"><span>Complimentary Pass for any 30-minute</span></div>

    <ul class="options">
      <li>Infrared Sauna + Red Light</li>
      <li>Velquist Compression</li>
      <li>Massage Chair</li>
      <li>Paraffin Wax Hand Bath</li>
    </ul>

    <div class="prices">
      <div class="row"><span class="label">Any 30 min session</span><span class="price">$40</span></div>
      <div class="row"><span class="label">Any 60 min session</span><span class="price">$65</span></div>
      <div class="row row--gap"><span class="label label--note">(15 minutes)</span><span class="price">$25</span></div>
    </div>

    <div class="person">
      <div class="person__name">Corinne Hale</div>
      <div class="person__role">Dr. Physical Therapy<br>Clinic Director</div>
      <div class="person__rule"></div>
    </div>

    <ul class="contact">
      <li><svg viewBox="0 0 24 24"><path d="M6.6 10.8a15.1 15.1 0 0 0 6.6 6.6l2.2-2.2c.3-.3.7-.4 1-.2 1.1.4 2.3.6 3.6.6.6 0 1 .4 1 1V20c0 .6-.4 1-1 1A17 17 0 0 1 3 4c0-.6.4-1 1-1h3.5c.6 0 1 .4 1 1 0 1.3.2 2.5.6 3.6.1.3 0 .7-.2 1z"/></svg><span class="phone">555-014-2290</span></li>
      <li><svg viewBox="0 0 24 24"><path d="M2 5h20v14H2z M2 5l10 8 10-8" fill="none" stroke="#ef5a3a" stroke-width="2.4"/></svg><span>desk@meridelptclinic.com</span></li>
      <li><svg viewBox="0 0 24 24"><circle cx="12" cy="12" r="9" fill="none" stroke="#ef5a3a" stroke-width="2"/><path d="M3 12h18M12 3c3 3 3 15 0 18M12 3c-3 3-3 15 0 18" fill="none" stroke="#ef5a3a" stroke-width="1.6"/></svg><span>meridelptclinic.com</span></li>
    </ul>

    <div class="address">
      <div class="address__label">Clinic</div>
      418 Alder Street Suite 210<br>Fernwood, Oregon 97000
    </div>

    <div class="footer-band">
      <svg width="64" height="34" viewBox="0 0 64 34"><path d="M12 0H52L64 34H0Z" fill="#fdfcfd"/></svg>
    </div>
  </section>

</body>
</html>
```